Traditional style Skull and crossbones craftsmans card for making custom works home decor and more

Brovik Works surrounding a skull and cross bones. Street address is 318 Marlow Ave N Essex ON. Email is BrovikWorks@mailvane.com and telephone number will be 519-430-6185. Use the attached image as a guideline would also like Support your local artist on the card. Our names are Dale and Morgan Brovik

Industry/Entity Type

It Support

Contact Information for Business Card

Standard size with a traditional style font

Font styles to use
Decorative
Script

Requirements
Must have
• 318 Marlow Ave. N Essex ON
• 519-430-6185
• Brovikworks@mailvane.com
• Welding
• Dale and Morgan Brovik
• Support your local artist
Nice to have
• Refer to images for ideas

```html
<!DOCTYPE html>
<html lang="en">
<head>
<meta charset="utf-8">
<title>Brovik Works – Business Card</title>
<link rel="stylesheet" href="https://fonts.googleapis.com/css2?family=UnifrakturCook:wght@700&display=swap">
<style>
  :root {
    --backdrop: #e8e6e2;
    --card: #0e0e0e;
    --silver: #a9a9a9;
    --amber: #f2a01c;
    --shadow: rgba(0, 0, 0, 0.28);
  }
  * { box-sizing: border-box; margin: 0; padding: 0; }
  html, body {
    width: 1200px;
    height: 959px;
    overflow: hidden;
    background: var(--backdrop);
  }
  .canvas {
    width: 1200px;
    height: 959px;
    display: flex;
    align-items: center;
    justify-content: center;
    gap: 40px;
  }
  .card {
    position: relative;
    width: 540px;
    height: 309px;
    background: var(--card);
    box-shadow: 0 14px 30px var(--shadow);
    font-family: "UnifrakturCook", serif;
    font-weight: 700;
    overflow: hidden;
  }

  /* Back: contact details */
  .card-back {
    display: flex;
    flex-direction: column;
    align-items: center;
    justify-content: center;
    text-align: center;
    padding: 20px 24px;
  }
  .tagline {
    color: var(--silver);
    font-size: 20px;
    letter-spacing: 1.5px;
    margin-bottom: 8px;
  }
  .flourish {
    display: block;
    width: 26px;
    height: 5px;
    border-radius: 3px;
    background: var(--amber);
    margin: 4px auto;
  }
  .contact {
    list-style: none;
    color: var(--amber);
    font-size: 18px;
    line-height: 1.15;
    letter-spacing: 0.5px;
  }
  .services {
    color: var(--silver);
    font-size: 18px;
    line-height: 1.25;
    letter-spacing: 1px;
    margin-top: 12px;
  }
  .amp { color: var(--amber); }

  /* Front: brand */
  .card-front {
    display: flex;
    flex-direction: column;
    align-items: center;
    justify-content: center;
    text-align: center;
    padding: 24px 60px;
  }
  .brand {
    display: flex;
    align-items: center;
    gap: 16px;
  }
  .brand-mark {
    width: 60px;
    height: 60px;
    border-radius: 50%;
    background: var(--amber);
  }
  .brand-name {
    color: var(--amber);
    font-size: 44px;
    line-height: 1;
  }
  .owners {
    color: var(--silver);
    font-size: 18px;
    letter-spacing: 1px;
    margin-top: 22px;
  }
  .motto {
    color: var(--amber);
    font-size: 16px;
    letter-spacing: 1.5px;
    margin-top: 8px;
  }
  .side-title {
    position: absolute;
    top: 50%;
    color: var(--silver);
    font-size: 15px;
    letter-spacing: 6px;
    white-space: nowrap;
  }
  .side-title-left {
    left: 28px;
    transform: translate(-50%, -50%) rotate(-90deg);
  }
  .side-title-right {
    right: 28px;
    transform: translate(50%, -50%) rotate(90deg);
  }
</style>
</head>
<body>
<main class="canvas">
  <section class="card card-back" aria-label="Card back">
    <p class="tagline">Specializing in “One of a Kind” Designs</p>
    <span class="flourish" role="img" aria-label="Small ornament"></span>
    <ul class="contact">
      <li>318 Marlow Ave. N Essex ON</li>
      <li>BrovikWorks@mailvane.com</li>
      <li>519-430-6185</li>
    </ul>
    <span class="flourish" role="img" aria-label="Small ornament"></span>
    <p class="services">
      Blacksmithing <span class="amp">&amp;</span> Custom Welding<br>
      Designing <span class="amp">&amp;</span> Sculpting <span class="amp">&amp;</span> Building
    </p>
  </section>

  <section class="card card-front" aria-label="Card front">
    <span class="side-title side-title-left">Designer</span>
    <div class="brand">
      <span class="brand-mark"></span>
      <span class="brand-name">Brovik Works</span>
    </div>
    <p class="owners">Dale and Morgan Brovik</p>
    <p class="motto">Support your local artist</p>
    <span class="side-title side-title-right">Craftsman</span>
  </section>
</main>
</body>
</html>
```